Unisex deodorant packaging

we need 12 designs of Unisex deodorant spray, all designs shoud be different.

Brand Name is Verdel. Artwork file size is attached for reference. Logo we can be redesigned.

variants names will be:

Tapestry
Ripple
Lanterns
Meadow
Quarry
Pebble
Tide
Fern
Orchard
Mossy
Vast
Brisk

Target Market(s)

B+, B, C+

Requirements
Must have
• colors, new fonts
Nice to have
• creative work, all 12 designs different

```html
<!DOCTYPE html>
<html lang="en">
<head>
<meta charset="utf-8">
<title>Verdel Tapestry Deodorant Body Spray Label</title>
<link rel="stylesheet" href="https://fonts.googleapis.com/css2?family=Dosis:wght@500;600&family=Oswald:wght@700&family=Archivo:wght@700&display=swap">
<style>
  :root {
    --page-bg: #141813;
    --label-black: #0d0e0d;
    --label-sheen: #1b1d1b;
    --brand-green: #2fd52b;
    --band-green: #1f8a1d;
    --deep-green: #0f4a0e;
    --text-light: #e4e6e4;
    --chevron-white: #d9dcd9;
    --accent-red: #d8201c;
  }
  * { box-sizing: border-box; margin: 0; padding: 0; }
  html, body {
    width: 1192px;
    height: 1200px;
    overflow: hidden;
    background: var(--page-bg);
  }
  .canvas {
    position: relative;
    width: 1192px;
    height: 1200px;
  }
  .label {
    position: absolute;
    left: 454px;
    top: 45px;
    width: 284px;
    height: 1110px;
    background: linear-gradient(90deg, var(--label-black) 0%, var(--label-sheen) 45%, var(--label-black) 100%);
    overflow: hidden;
  }
  .label-art {
    position: absolute;
    inset: 0;
  }
  .brand-name {
    position: absolute;
    top: 138px;
    left: 0;
    width: 100%;
    text-align: center;
    font-family: "Oswald", sans-serif;
    font-weight: 700;
    font-size: 58px;
    letter-spacing: 1px;
    color: var(--brand-green);
  }
  .claim {
    position: absolute;
    top: 286px;
    left: 0;
    width: 100%;
    text-align: center;
    font-family: "Dosis", sans-serif;
    font-weight: 500;
    font-size: 25px;
    color: var(--text-light);
  }
  .hero-figure {
    position: absolute;
    left: 66px;
    top: 393px;
    width: 130px;
    height: 160px;
    border-radius: 6px;
    background: radial-gradient(ellipse at 50% 45%, #c81d18 0%, #7a1210 50%, rgba(13,14,13,0) 75%);
  }
  .variant-name {
    position: absolute;
    top: 836px;
    left: 0;
    width: 100%;
    text-align: center;
    font-family: "Dosis", sans-serif;
    font-weight: 500;
    font-size: 54px;
    line-height: 1;
    color: var(--brand-green);
  }
  .product-type {
    position: absolute;
    top: 920px;
    left: 0;
    width: 100%;
    display: flex;
    justify-content: center;
    font-family: "Dosis", sans-serif;
    font-weight: 500;
    font-size: 23px;
    color: var(--text-light);
  }
  .product-type span { padding: 0 6px; }
  .product-type span + span { border-left: 2px solid var(--brand-green); }
  .net-content {
    position: absolute;
    top: 1020px;
    left: 0;
    width: 100%;
    display: flex;
    justify-content: center;
    gap: 22px;
    font-family: "Archivo", sans-serif;
    font-weight: 700;
    color: var(--text-light);
  }
  .net-content .volume { font-size: 15px; }
  .net-content .ounces { font-size: 12px; padding-top: 2px; }
</style>
</head>
<body>
<main class="canvas">
  <section class="label">
    <svg class="label-art" width="284" height="1110" viewBox="0 0 284 1110" aria-hidden="true">
      <defs>
        <linearGradient id="stripe-fade" x1="0" y1="0" x2="0" y2="1">
          <stop offset="0" stop-color="#2fd52b" stop-opacity="0.9"/>
          <stop offset="1" stop-color="#2fd52b" stop-opacity="0"/>
        </linearGradient>
        <linearGradient id="band-fill" x1="0" y1="0" x2="0" y2="1">
          <stop offset="0" stop-color="#1f8a1d"/>
          <stop offset="1" stop-color="#0f4a0e"/>
        </linearGradient>
      </defs>
      <!-- green chevron band: V top edge, peaked bottom edge -->
      <polygon class="chevron-band" points="0,470 142,555 284,470 284,700 142,605 0,700" fill="url(#band-fill)"/>
      <!-- white chevron -->
      <polyline class="chevron" points="0,440 142,525 284,440" fill="none" stroke="var(--chevron-white)" stroke-width="7"/>
      <!-- side rails -->
      <rect x="8" y="600" width="10" height="330" fill="var(--band-green)"/>
      <rect x="266" y="600" width="10" height="330" fill="var(--band-green)"/>
      <!-- vertical drips, ending above the variant name -->
      <rect x="86" y="610" width="3" height="200" fill="url(#stripe-fade)"/>
      <rect x="115" y="600" width="3" height="210" fill="url(#stripe-fade)"/>
      <rect x="168" y="600" width="3" height="210" fill="url(#stripe-fade)"/>
      <rect x="198" y="610" width="3" height="200" fill="url(#stripe-fade)"/>
      <!-- red accent ticks -->
      <rect x="133" y="790" width="5" height="34" fill="var(--accent-red)"/>
      <rect x="150" y="790" width="5" height="34" fill="var(--accent-red)"/>
      <!-- underline -->
      <rect x="20" y="914" width="244" height="3" fill="var(--brand-green)"/>
      <!-- edge arrows -->
      <polygon points="0,928 10,918 10,938" fill="var(--chevron-white)"/>
      <polygon points="284,928 274,918 274,938" fill="var(--chevron-white)"/>
    </svg>

    <div class="brand-name">Verdel</div>
    <div class="claim">French Perfumed</div>
    <div class="hero-figure" role="img" aria-label="Illustration of a leaping figure in a red suit"></div>
    <div class="variant-name">Tapestry</div>
    <div class="product-type"><span>Deodrant</span><span>Body</span><span>Spray</span></div>
    <div class="net-content"><span class="volume">150ml</span><span class="ounces">Net5.1 fl. oz.</span></div>
  </section>
</main>
</body>
</html>
```